Brisbane IT support business needs our first website

Hi All,

We are after a new website design for our IT solutions and support business.The business name is Harlow Digital Systems Group, or HDSG for short. We provide a range of solutions and services within the IT space.

I would like to utilize the two colours in our business logo I have uploaded.

I understand this is initially for the design only aspect of the site, but I would like to engage the winner to finish coding the website and finalize after also.

Target Market(s)

Other businesses owners and home users.

Industry/Entity Type

Business

Requirements
Must have
• Nice clean and functional design utilizing our business colours from the logo.

```html
<!DOCTYPE html>
<html lang="en">
<head>
<meta charset="utf-8">
<title>Harlow Digital Systems Group</title>
<link rel="stylesheet" href="https://fonts.googleapis.com/css2?family=Open+Sans:wght@300;400;600;700&display=swap">
<style>
:root{
  --orange:#ee7b22;
  --orange-dark:#d8661a;
  --teal:#0f6c86;
  --teal-dark:#0b5a71;
  --white:#ffffff;
  --ink:#222222;
  --grey-text:#6a6a6a;
  --light-bg:#f6f6f6;
  --field:#e9e5e3;
  --dark-btn:#2b2b2b;
}
*{box-sizing:border-box;margin:0;padding:0}
html,body{width:825px;height:1200px;overflow:hidden}
body{position:relative;font-family:"Open Sans",Arial,sans-serif;color:var(--ink);background:var(--white)}
.abs{position:absolute}

/* Hero */
.hero{left:0;top:0;width:825px;height:424px;overflow:hidden}
.hero-photo{position:absolute;inset:0;background:
  radial-gradient(ellipse 180px 90px at 400px 360px,rgba(70,180,230,.55),transparent 70%),
  radial-gradient(ellipse 120px 70px at 520px 150px,rgba(60,170,225,.45),transparent 70%),
  radial-gradient(ellipse 320px 420px at 410px 240px,#1b2230 0%,#2a3038 55%,transparent 80%),
  linear-gradient(90deg,#8b8b8b 0%,#4a4a4a 25%,#2b2b2b 50%,#4a4a4a 75%,#8d8d8d 100%)}
.brand-name{left:70px;top:40px;font-size:20px;font-weight:600;color:var(--white);letter-spacing:1px}
.nav{left:68px;top:0;width:689px;height:73px;border-bottom:1px solid rgba(255,255,255,.7)}
.nav-item{position:absolute;top:48px;font-size:9px;font-weight:600;color:var(--white);text-transform:uppercase}
.nav-item.active{color:var(--orange)}
.nav-underline{position:absolute;left:217px;top:70px;width:70px;height:3px;background:var(--orange)}
.hero-title{left:0;width:825px;top:154px;text-align:center;color:var(--white);font-weight:400;font-size:40px;line-height:44px}
.hero-rule{left:165px;top:303px;width:495px;height:1px;background:rgba(255,255,255,.75)}
.dots{left:378px;top:368px;display:flex;gap:4px}
.dot{width:14px;height:14px;border-radius:50%;background:var(--white)}
.dot.active{background:var(--orange)}

/* Services */
.services{left:0;top:424px;width:825px;height:202px;background:var(--orange)}
.notch{left:400px;top:424px}
.service{position:absolute;top:25px;width:176px;text-align:center;color:var(--white)}
.service-icon{width:52px;height:52px;border-radius:50%;background:var(--white);margin:0 auto;display:flex;align-items:center;justify-content:center}
.service-title{margin-top:14px;font-size:14.5px;font-weight:400;letter-spacing:1.5px;line-height:18px;text-transform:uppercase}
.service-text{margin-top:7px;font-size:9.6px;font-weight:600;line-height:13px}

/* Promo */
.promo{left:0;top:626px;width:825px;height:97px;background:linear-gradient(90deg,var(--teal),var(--teal-dark) 50%,var(--teal))}
.promo-text{position:absolute;left:68px;top:30px;color:var(--white);font-size:22px;font-weight:300}
.promo-text strong{font-weight:600}
.promo-text .big{font-size:28px;font-weight:700}
.promo-btn{position:absolute;left:644px;top:33px;width:113px;height:32px;background:var(--white);color:var(--ink);font-size:9.5px;display:flex;align-items:center;justify-content:center}

/* Testimonials */
.testimonials{left:0;top:723px;width:825px;height:169px;background:var(--light-bg)}
.testi-bar{position:absolute;left:69px;top:37px;width:3px;height:96px;background:var(--orange)}
.testi-title{position:absolute;left:85px;top:30px;font-size:19px;font-weight:700;color:var(--ink)}
.quote-mark{position:absolute;left:84px;top:60px;font-size:44px;line-height:44px;color:#f3c6a0;font-family:Georgia,serif}
.testi-text{position:absolute;left:113px;top:74px;width:646px;font-size:8.2px;line-height:14.5px;color:var(--grey-text)}
.testi-author{position:absolute;left:632px;top:128px;font-size:9px;color:var(--orange);display:flex;align-items:center;gap:10px}
.testi-author::before,.testi-author::after{content:"";width:26px;height:1px;background:#cfcfcf}

/* Newsletter */
.newsletter{left:0;top:892px;width:825px;height:52px;background:var(--orange)}
.news-label{position:absolute;left:136px;top:13px;font-size:11px;font-weight:600;line-height:13px;color:var(--white)}
.field-input{position:absolute;top:14px;width:176px;height:26px;background:var(--white);font-size:8px;color:#999;padding:8px 12px}
.news-btn{position:absolute;left:634px;top:14px;width:86px;height:26px;background:var(--dark-btn);color:var(--white);font-size:9.5px;font-weight:700;display:flex;align-items:center;justify-content:center}

/* Footer */
.footer{left:0;top:944px;width:825px;height:224px;background:linear-gradient(90deg,var(--teal),var(--teal-dark) 50%,var(--teal))}
.foot-heading{position:absolute;font-size:13px;font-weight:400;color:var(--white);text-transform:uppercase}
.social{position:absolute;left:70px;top:47px;display:flex;gap:8px}
.social-dot{width:26px;height:26px;border-radius:50%;background:#5b5b5b}
.social-dot.first{background:var(--orange)}
.blog{position:absolute;left:70px;top:124px;width:185px;color:var(--white)}
.blog-title{font-size:9.5px;font-weight:700}
.blog-date{font-size:6px}
.blog-text{font-size:8.5px;line-height:13px;margin-top:2px}
.blog-more{font-size:8.5px;font-weight:700;margin-top:5px}
.ad-list{position:absolute;left:301px;top:44px;width:189px;list-style:none}
.ad-list li{height:17.3px;border-bottom:1px solid rgba(255,255,255,.55);font-size:7.5px;font-weight:700;color:var(--white);padding:4px 0 0 9px;position:relative}
.ad-list li::before{content:"";position:absolute;left:1px;top:8px;width:3px;height:3px;background:rgba(255,255,255,.6)}
.contact-field{position:absolute;left:557px;width:190px;background:var(--field);font-size:8px;color:#888;padding:5px 6px;font-family:Georgia,serif}
.contact-btn{position:absolute;left:557px;top:183px;width:51px;height:18px;background:var(--dark-btn);color:var(--white);font-size:8.5px;font-weight:700;display:flex;align-items:center;justify-content:center}

/* Bottom bar */
.bottom-bar{left:0;top:1168px;width:825px;height:32px;background:var(--orange)}
.copyright{position:absolute;left:63px;top:11px;font-size:8.5px;color:var(--white)}
</style>
</head>
<body>

<header class="abs hero">
  <div class="hero-photo" role="img" aria-label="Blurred photo of a businessman in a suit holding a tablet with glowing blue app icons"></div>
  <nav class="abs nav">
    <span class="nav-item active" style="left:238px">Home</span>
    <span class="nav-item" style="left:328px">About us</span>
    <span class="nav-item" style="left:435px">Services</span>
    <span class="nav-item" style="left:538px">Blog</span>
    <span class="nav-item" style="left:627px">Contacts</span>
    <span class="nav-underline"></span>
  </nav>
  <span class="abs brand-name">HDSG</span>
  <h1 class="abs hero-title">Networking.<br>Database management.<br>Application development.</h1>
  <div class="abs hero-rule"></div>
  <div class="abs dots"><span class="dot active"></span><span class="dot"></span><span class="dot"></span><span class="dot"></span></div>
</header>

<section class="abs services">
  <div class="service" style="left:60px">
    <div class="service-icon"><svg width="22" height="22" viewBox="0 0 22 22"><circle cx="11" cy="11" r="9" fill="none" stroke="#ee7b22" stroke-width="2.2"/><path d="M2 11h18M11 2c-4 4-4 14 0 18M11 2c4 4 4 14 0 18" fill="none" stroke="#ee7b22" stroke-width="1.6"/></svg></div>
    <h2 class="service-title">Web<br>Development</h2>
    <p class="service-text">Praesent vestibulum aenean nonummy hendrerit mauris. Hasellus porta. Fusce suscipit varius mi. Cum sociis natoque penatibus magnis dis.</p>
  </div>
  <div class="service" style="left:236px">
    <div class="service-icon"><svg width="22" height="22" viewBox="0 0 22 22"><circle cx="9" cy="9" r="4.5" fill="none" stroke="#ee7b22" stroke-width="3" stroke-dasharray="2.5 1.5"/><circle cx="9" cy="9" r="1.6" fill="#ee7b22"/><circle cx="16" cy="16" r="3" fill="none" stroke="#ee7b22" stroke-width="2.2" stroke-dasharray="2 1.3"/></svg></div>
    <h2 class="service-title">Technical<br>Support</h2>
    <p class="service-text">Praesent vestibulum aenean nonummy hendrerit mauris. Hasellus porta. Fusce suscipit varius mi. Cum sociis natoque penatibus magnis dis.</p>
  </div>
  <div class="service" style="left:412px">
    <div class="service-icon"><svg width="22" height="22" viewBox="0 0 22 22"><circle cx="11" cy="8" r="5.5" fill="#ee7b22"/><rect x="8.5" y="13" width="5" height="3" fill="#ee7b22"/><rect x="9" y="17" width="4" height="2" fill="#ee7b22"/></svg></div>
    <h2 class="service-title">Network<br>Solutions</h2>
    <p class="service-text">Praesent vestibulum aenean nonummy hendrerit mauris. Hasellus porta. Fusce suscipit varius mi. Cum sociis natoque penatibus magnis dis.</p>
  </div>
  <div class="service" style="left:587px">
    <div class="service-icon"><svg width="22" height="22" viewBox="0 0 22 22"><path d="M2 5h7l2 2h9v11H2z" fill="#ee7b22"/></svg></div>
    <h2 class="service-title">Database<br>Management</h2>
    <p class="service-text">Praesent vestibulum aenean nonummy hendrerit mauris. Hasellus porta. Fusce suscipit varius mi. Cum sociis natoque penatibus magnis dis.</p>
  </div>
</section>
<svg class="abs notch" width="26" height="13" viewBox="0 0 26 13"><path d="M0 0h26L13 13z" fill="#2a2a2a"/><path d="M3 0h20L13 10z" fill="#d8661a"/></svg>

<section class="abs promo">
  <p class="promo-text">Get <strong>FREE</strong> month of online technical support <span class="big">24/7</span></p>
  <span class="promo-btn">Read more</span>
</section>

<section class="abs testimonials">
  <span class="testi-bar"></span>
  <h2 class="testi-title">Testimonials</h2>
  <span class="quote-mark">&ldquo;</span>
  <p class="testi-text">Lorem ipsum dolor sit amet, consectetur adipiscing elit. Praesent quis sodales libero. Quisque et pharetra arcu, mattis ultricies erat. Duis elit erat, viverra at tellueget.facbus facilisis augue. Pellentesque laciniaortor at tellus pellsque rutrum. Fusce id risus risus. Maecenas tempus, auctor felis icursus tortor. Quisque pulvinar neque mattis, tporqel vitae, pellentesque ipsum.Pellentesque rhoncus consectetur augue at rhoncus. Aenean pharetra libero sed massa rhoncus varius. Suspendisse consequat interdum orcietli vitae bibendum nulla vestibulum sed. Praesent vitae neque ac velit pellentesque iaculis et in nisi.</p>
  <span class="testi-author">Maria Holt</span>
</section>

<section class="abs newsletter">
  <svg class="abs" style="left:94px;top:13px" width="26" height="26" viewBox="0 0 26 26"><path d="M1 12L25 1 19 24 12 16zM12 16L25 1M12 16v8l3-5" fill="none" stroke="#fff" stroke-width="1.4" stroke-linejoin="round"/></svg>
  <p class="news-label">Subscribe to<br>our Newsletter</p>
  <span class="field-input" style="left:253px">Enter Your Name</span>
  <span class="field-input" style="left:443px">Enter Your Email Address</span>
  <span class="news-btn">SUBSCRIBE</span>
</section>

<footer class="abs footer">
  <h3 class="foot-heading" style="left:70px;top:19px">Social Links</h3>
  <div class="social"><span class="social-dot first"></span><span class="social-dot"></span><span class="social-dot"></span></div>
  <h3 class="foot-heading" style="left:70px;top:99px">Blogs</h3>
  <div class="blog">
    <p class="blog-title">Post Title</p>
    <p class="blog-date">Friday, 6th April 2014</p>
    <p class="blog-text">Lorem ipsum dolor sit amet, consectetur adipiscing elit. Nunc non diam erat. In fringilla massa ut nisi ullamcorper pellentesque.</p>
    <p class="blog-more">Read More &raquo;</p>
  </div>

  <h3 class="foot-heading" style="left:301px;top:19px">Advertise with us</h3>
  <ul class="ad-list">
    <li>Lorem ipsum dolor sit</li>
    <li>Amet consectetur</li>
    <li>Praesent vel sem id</li>
    <li>Curabitur hendrerit est</li>
    <li>Aliquam eget erat nec sapien</li>
    <li>Cras id augue nunc</li>
    <li>In nec justo non</li>
    <li>Vivamus mollis enim ut</li>
    <li>Curabitur hendrerit est</li>
  </ul>

  <h3 class="foot-heading" style="left:557px;top:19px">Contact us</h3>
  <span class="contact-field" style="top:45px;height:20px">Name</span>
  <span class="contact-field" style="top:71px;height:20px">Email</span>
  <span class="contact-field" style="top:96px;height:81px">Massages</span>
  <span class="contact-btn">SUBMIT</span>
</footer>

<div class="abs bottom-bar"><p class="copyright">Copyright &copy; 2014 - All Rights Reserved</p></div>

</body>
</html>
```